Verelin Publishing

I made a website myself www.verelinpublishing.co.uk a few years ago but I need a new design, which I will code. One that I can be proud of, that 's sexy, to win new customers and showcase my publishing skills. This is a publishing website so I want the home page and books page to be fantastic. I have a logo already so will like the same colour scheme or thereabouts. I have current files and features that I would like to add to your creativity and experience.

Target Market(s)

Web Designers, Graphic Designers

Industry/Entity Type

Book Publisher

Number of Pages Required

5+ page

Font styles to use
Sans Serif

Colors
0255a3
ffffff
ec1f27

Requirements
Must have
• Menu and Sub Menu
• Footer
• Buy Page - Shopping Cart
• Upload feature on the submissions page
• video section on home page (how we publish books)
• Ad space section
Nice to have
• social media bar
• Zoom in page

```html
<!DOCTYPE html>
<html lang="en">
<head>
<meta charset="utf-8">
<title>Verelin Publishing – Self-Publishing That Works</title>
<link href="https://fonts.googleapis.com/css2?family=Open+Sans:wght@300;400;600;700&display=swap" rel="stylesheet">
<style>
:root{
  --blue:#0255a3;
  --red:#ec1f27;
  --white:#ffffff;
  --ink:#4a4a4a;
  --muted:#8a8a8a;
  --line:#e3e3e3;
  --panel:#f1f2f4;
  --band:#f4f4f4;
  --footer:#241c6b;
  --footer-text:#c9c6e6;
  --social:#3a5f9e;
}
*{box-sizing:border-box;margin:0;padding:0}
html,body{width:1200px;height:2456px;overflow:hidden;background:var(--white)}
body{position:relative;font-family:"Open Sans",Arial,sans-serif;color:var(--ink)}
.abs{position:absolute}

/* header */
.site-header{left:0;top:0;width:1200px;height:120px;background:var(--white)}
.brand{left:120px;top:40px;display:flex;align-items:center;gap:12px}
.brand-mark{width:22px;height:22px;background:var(--red);border-radius:50%}
.brand-name{font-size:27px;font-weight:700;color:var(--blue);letter-spacing:-.3px}
.main-nav{right:118px;top:50px;display:flex;gap:34px;font-size:14px;color:#666}
.main-nav .active{color:var(--red)}

/* hero */
.hero{left:0;top:120px;width:1200px;height:490px;background:linear-gradient(100deg,#eceae6 0%,#dcd9d3 45%,#c9c3ba 70%,#a59c90 100%);overflow:hidden}
.hero-photo{right:0;top:0;width:560px;height:490px;background:radial-gradient(ellipse at 60% 40%,#d8cfc3 0%,#b3a898 55%,#8d8172 100%)}
.hero-book{left:160px;top:62px;width:270px;height:420px;background:linear-gradient(160deg,#2e3a52,#1c2538 60%,#c0392b 100%);box-shadow:8px 10px 18px rgba(0,0,0,.3)}
.hero-copy{left:560px;top:170px;width:420px;text-align:center;color:var(--white)}
.hero-title{font-size:30px;font-weight:600;text-shadow:0 1px 3px rgba(0,0,0,.35)}
.hero-sub{font-size:30px;font-weight:600;margin-top:4px;text-shadow:0 1px 3px rgba(0,0,0,.35)}
.btn{display:inline-block;background:var(--blue);color:var(--white);font-size:15px;font-weight:600;padding:10px 22px;border-radius:3px;margin-top:30px}
.slider-arrow{top:230px;width:28px;height:28px;border-radius:50%;background:rgba(255,255,255,.55)}
.social-bar{left:0;top:252px;width:40px}
.social-bar span{display:block;width:40px;height:40px;margin-bottom:2px;background:var(--social)}

/* intro */
.intro{left:0;top:670px;width:1200px;text-align:center}
.section-title{font-size:26px;font-weight:600;color:var(--red)}
.intro p{width:900px;margin:16px auto 0;font-size:14px;line-height:22px;color:var(--ink)}
.feature-row{left:132px;top:792px;display:flex;gap:14px}
.feature{width:304px;height:160px;background:var(--panel);text-align:center;padding-top:30px}
.feature svg{width:60px;height:60px}
.feature-label{margin-top:16px;font-size:22px;font-weight:700;color:var(--blue);letter-spacing:.5px}

/* video */
.video{left:0;top:1024px;width:1200px;height:282px;background:linear-gradient(90deg,#c9c3b8,#a99f90 55%,#8f8576);overflow:hidden}
.video-copy{left:0;top:90px;width:1200px;text-align:center;color:var(--white)}
.play{width:64px;height:64px;margin:0 auto}
.video-copy h3{font-size:22px;font-weight:600;margin-top:12px;text-shadow:0 1px 3px rgba(0,0,0,.4)}

/* steps */
.steps-title{left:0;top:1380px;width:1200px;text-align:center}
.steps{left:132px;top:1448px;width:936px;display:grid;grid-template-columns:456px 456px;gap:28px 24px}
.step{height:144px;border:1px solid var(--line);padding:18px 22px;box-shadow:0 1px 3px rgba(0,0,0,.05)}
.step h4{display:flex;align-items:center;gap:10px;font-size:20px;font-weight:600;color:var(--blue)}
.step h4 svg{width:20px;height:20px}
.step p{margin-top:10px;font-size:12px;line-height:19px;color:var(--muted)}

/* partners */
.partners-title{left:0;top:1876px;width:1200px;text-align:center;font-size:26px;font-weight:600;color:#7a7a7a}
.partner-row{left:120px;top:1944px;width:960px;display:flex;justify-content:space-between;align-items:center}
.partner{font-size:20px;font-weight:600;color:#6d6d6d}

/* testimonials */
.testimonials{left:0;top:2020px;width:1200px;height:300px;background:var(--band);text-align:center}
.testimonials h2{margin-top:62px;font-size:26px;font-weight:600;color:var(--red)}
.t-name{margin-top:10px;font-size:12px;color:var(--muted)}
.t-quote{margin-top:10px;font-size:15px;color:#666}
.avatar{width:56px;height:56px;border-radius:50%;margin:18px auto 0;background:radial-gradient(circle at 50% 40%,#b08a6e,#6f5140)}

/* footer */
.site-footer{left:0;top:2336px;width:1200px;height:120px;background:var(--footer);color:var(--footer-text)}
.f-brand{left:130px;top:45px;display:flex;align-items:center;gap:10px}
.f-brand .brand-mark{width:16px;height:16px}
.f-brand span{font-size:20px;font-weight:700;color:var(--white)}
.f-cols{left:490px;top:26px;display:flex;gap:70px;font-size:12px;line-height:22px}
.f-copy{right:120px;top:28px;font-size:11px;line-height:20px;text-align:left}
</style>
</head>
<body>

<header class="site-header abs">
  <div class="brand abs"><span class="brand-mark"></span><span class="brand-name">Verelin Publishing</span></div>
  <nav class="main-nav abs">
    <span class="active">Home</span><span>Publishing</span><span>Submissions</span><span>Books</span><span>Authors</span><span>Services</span><span>Contact</span>
  </nav>
</header>

<section class="hero abs">
  <div class="hero-photo abs" role="img" aria-label="Photo of a smiling woman reading a book"></div>
  <div class="hero-book abs" role="img" aria-label="Featured book cover"></div>
  <div class="hero-copy abs">
    <div class="hero-title">Verelin Publishing</div>
    <div class="hero-sub">Self-Publishing That Works</div>
    <span class="btn">Submit Book</span>
  </div>
  <span class="slider-arrow abs" style="left:26px"></span>
  <span class="slider-arrow abs" style="right:26px"></span>
  <div class="social-bar abs" aria-label="Share buttons">
    <span></span><span></span><span></span><span></span><span></span>
  </div>
</section>

<section class="intro abs">
  <h2 class="section-title">Have a story to tell? We can help you publish your book.</h2>
  <p>Welcome to Verelin Publishing, we are an independent publishing company located in London/Surrey. We publish Trade Fiction and non-fiction, &amp; Young Adult (YA) in a variety of subjects.</p>
</section>

<div class="feature-row abs">
  <div class="feature">
    <svg viewBox="0 0 60 60" fill="none" stroke="#0255a3" stroke-width="2.5"><path d="M8 12h18c3 0 4 2 4 4v34c0-2-1-4-4-4H8z"/><path d="M52 12H34c-3 0-4 2-4 4v34c0-2 1-4 4-4h18z"/><path d="M13 20h11M13 27h11M13 34h11M36 20h11M36 27h11M36 34h11"/></svg>
    <div class="feature-label">BOOK</div>
  </div>
  <div class="feature">
    <svg viewBox="0 0 60 60" fill="none" stroke="#0255a3" stroke-width="2.5"><circle cx="30" cy="20" r="8"/><path d="M16 46c0-9 6-14 14-14s14 5 14 14"/><circle cx="13" cy="24" r="5"/><circle cx="47" cy="24" r="5"/><path d="M4 44c0-6 4-10 9-10M56 44c0-6-4-10-9-10"/></svg>
    <div class="feature-label">AUTHORS</div>
  </div>
  <div class="feature">
    <svg viewBox="0 0 60 60" fill="none" stroke="#0255a3" stroke-width="2.5"><path d="M30 8 52 20 30 32 8 20z"/><path d="M8 30l22 12 22-12"/><path d="M8 40l22 12 22-12"/></svg>
    <div class="feature-label">SUBMISSIONS</div>
  </div>
</div>

<section class="video abs" role="img" aria-label="Video still of hands writing in a notebook">
  <div class="video-copy abs">
    <svg class="play" viewBox="0 0 64 64"><circle cx="32" cy="32" r="30" fill="rgba(255,255,255,.25)" stroke="#fff" stroke-width="2"/><path d="M26 20l18 12-18 12z" fill="#fff"/></svg>
    <h3>Learn How We Publish Books</h3>
  </div>
</section>

<div class="steps-title abs"><h2 class="section-title">Publish Your Book in 4 Easy Steps</h2></div>

<div class="steps abs">
  <div class="step">
    <h4><svg viewBox="0 0 20 20" fill="#0255a3"><path d="M3 14l9-9 3 3-9 9H3z"/><path d="M13 4l2-2 3 3-2 2z"/></svg>Writing</h4>
    <p>Your words are the heart of every book we make. Finish your draft, polish each chapter and shape the story you want readers to find. When you feel ready, the next step begins.</p>
  </div>
  <div class="step">
    <h4><svg viewBox="0 0 20 20" fill="#0255a3"><path d="M2 9l16-7-5 16-3-6z"/></svg>Submission</h4>
    <p>Send your finished manuscript through our upload page with a short synopsis and a few details about you. Our team reads every entry and replies within a few weeks of receiving it.</p>
  </div>
  <div class="step">
    <h4><svg viewBox="0 0 20 20" fill="none" stroke="#0255a3" stroke-width="2"><path d="M5 2h7l4 4v12H5z"/><path d="M8 10h5M8 13h5"/></svg>Contract</h4>
    <p>If your book is a good fit, we offer a clear contract that sets out the terms, timeline and support. Take your time to read it and ask questions before you decide to sign.</p>
  </div>
  <div class="step">
    <h4><svg viewBox="0 0 20 20" fill="none" stroke="#0255a3" stroke-width="2.2"><circle cx="8" cy="8" r="5"/><path d="M12 12l6 6"/></svg>Review</h4>
    <p>Our editors review your manuscript, suggest changes and work with you on the final text. Once it is approved, we prepare your book for print and release it to stores.</p>
  </div>
</div>

<div class="partners-title abs">Companies We Work With</div>
<div class="partner-row abs">
  <span class="partner">northmere.co.uk</span>
  <span class="partner">quillo</span>
  <span class="partner">Pagefold</span>
  <span class="partner">Leafshelf</span>
  <span class="partner">HARBOR &amp; VANE</span>
  <span class="partner">tarn</span>
</div>

<section class="testimonials abs">
  <h2>Testimonials</h2>
  <div class="t-name">Daniel Reyes</div>
  <div class="t-quote">“ You read our book and our editorial team helped it shine, then we all saw it released with pride. ”</div>
  <div class="avatar" role="img" aria-label="Portrait of the reviewer"></div>
</section>

<footer class="site-footer abs">
  <div class="f-brand abs"><span class="brand-mark"></span><span>Verelin Publishing</span></div>
  <div class="f-cols abs">
    <div>• Submissions<br>• Publishing<br>• Books</div>
    <div>• News<br>• Services<br>• Pages</div>
    <div>• Authors<br>• Contact<br>• Terms</div>
  </div>
  <div class="f-copy abs">Copyright © 2016 · Verelin Publishing<br>All rights reserved.<br>www.verelinpublishing.co.uk</div>
</footer>

</body>
</html>
```